Small, static, 2 page website that promotes 3-6 workshops

This is a microsite for my company that promotes 3 (and later 6) security workshops for developers. The address is going to be vakwerk-leerlijnen.nl so it is very important that the title reads 'Vakwerk Leerlijnen' and the subtitle reads 'voor ontwikkelaars' (means for developers in dutch).

On the frontpage, there will be a small introduction text (about 50 words) about the workshops in general and there should be 3 workshops listed on the frontpage with also a small introduction text. All the workshops are cyber security/hacking related so maybe a small graphic for every workshop would lighten things up.

Then when a visitor clicks a 'more info' button a detail page about that specific workshop with a longer description, a date/location, a 'book now' button and a price should be show.

I have include a quick drawing of what I have in mind for the frontpage, this is not set in stone so you could come up with something else.

I also included my company logo, it should be clear on the site that these workshops are 'Brightmoor Labs' workshops.

Target Market(s)

Development companies looking for security workshops, the responsible people for those type of workshops are usually security officers, lead developers/managers or developers themselves.

Industry/Entity Type

It Company

Number of Pages Required

2 page

Font styles to use
Sans Serif
Other font styles liked:
• Please choose a font you

Requirements
Must have
• 3 highlighted trainings on the frontpage and a detail page and the title and subtitle as headings on the page.
Nice to have
• I'd really like to have the 3 boxes on the frontpage to have icons or some sort of images. The first 3 workshops that are going to be on the page are:
• - Security awareness for developers
• - Web application security from a hackers perspective
• - Penetrationtesting for developers

```html
<!DOCTYPE html>
<html lang="nl">
<head>
<meta charset="utf-8">
<title>Brightmoor Labs – Vakwerk Leerlijnen voor ontwikkelaars</title>
<link href="https://fonts.googleapis.com/css2?family=Open+Sans:wght@400;600&display=swap" rel="stylesheet">
<style>
:root{
  --navy:#173a6a;
  --navy-dark:#0f2d57;
  --btn-top:#2a5790;
  --btn-bottom:#143c70;
  --ink:#222;
  --text:#666;
  --muted:#888;
  --line:#ddd;
  --panel:#efefef;
  --white:#fff;
  --hero-a:#e4e9ef;
  --hero-b:#b9c5d2;
}
*{margin:0;padding:0;box-sizing:border-box}
html,body{width:704px;height:1200px;overflow:hidden}
body{font-family:"Open Sans",sans-serif;background:var(--white);color:var(--text);position:relative}
.btn{display:inline-block;background:linear-gradient(var(--btn-top),var(--btn-bottom));color:var(--white);font-size:6.5px;border-radius:2px;text-align:center;text-decoration:none}

/* header */
.site-header{position:absolute;left:0;top:0;width:704px;height:66px;box-shadow:0 1px 3px rgba(0,0,0,.15);z-index:2;background:var(--white)}
.brand{position:absolute;left:78px;top:20px;display:flex;align-items:center;gap:7px}
.brand-mark{width:22px;height:22px;border-radius:50%;background:var(--navy)}
.brand-name{font-size:17px;font-weight:400;color:var(--navy);letter-spacing:.5px;line-height:1}
.main-nav{position:absolute;right:78px;top:0;display:flex;gap:0;height:66px}
.main-nav a{font-size:6.5px;color:var(--muted);text-decoration:none;text-transform:uppercase;line-height:68px;padding:0 12px;position:relative;letter-spacing:.2px}
.main-nav a:first-child{padding-left:0}
.main-nav a:last-child{padding-right:0}
.main-nav a.active{color:var(--navy)}
.main-nav a.active::after{content:"";position:absolute;left:0;right:12px;bottom:0;height:2px;background:var(--navy)}

/* hero */
.hero{position:absolute;left:0;top:66px;width:704px;height:267px;background:linear-gradient(110deg,var(--hero-a) 0%,#d3dbe4 45%,var(--hero-b) 100%)}
.hero-title{position:absolute;left:78px;top:94px;font-size:22px;font-weight:400;color:var(--ink);line-height:28px;text-transform:uppercase}
.hero-dots{position:absolute;left:333px;top:237px;display:flex;gap:6px}
.hero-dots span{width:8px;height:8px;border-radius:50%;background:#999}
.hero-dots span.on{background:var(--navy)}

/* welcome */
.welcome{position:absolute;left:78px;top:333px;width:548px;text-align:center}
.welcome h1{margin-top:25px;font-size:20px;font-weight:400;color:var(--navy);text-transform:uppercase}
.welcome p{margin-top:12px;font-size:6px;line-height:14px}
.welcome .btn{margin-top:16px;width:59px;height:21px;line-height:21px}

/* trainings */
.trainings{position:absolute;left:0;top:506px;width:704px;height:512px;background:var(--panel)}
.training-grid{position:absolute;left:78px;top:44px;display:grid;grid-template-columns:170px 170px 171px;column-gap:19px;row-gap:24px}
.training-card{height:202px;background:var(--white);box-shadow:0 1px 4px rgba(0,0,0,.18);text-align:center;padding-top:18px}
.training-card svg{height:28px;width:32px;display:block;margin:0 auto}
.training-card h2{margin-top:18px;font-size:12px;font-weight:400;color:var(--navy-dark);text-transform:uppercase}
.training-card p{margin:14px 8px 0;font-size:5.6px;line-height:14px}
.training-card .btn{margin-top:16px;width:59px;height:21px;line-height:21px}

/* footer */
.site-footer{position:absolute;left:0;top:1018px;width:704px;height:182px}
.site-footer .brand{top:26px}
.social{position:absolute;left:76px;top:87px;display:flex;gap:4px}
.social span{width:18px;height:18px;border:1px solid #555;border-radius:50%}
.footer-col{position:absolute;top:27px}
.footer-col h3{font-size:8.5px;font-weight:400;color:var(--navy);text-transform:uppercase}
.quick-links{left:274px}
.quick-links ul{list-style:none;margin-top:8px}
.quick-links li{font-size:6px;line-height:14px}
.contact{left:365px}
.contact ul{list-style:none;margin-top:8px}
.contact li{font-size:6px;line-height:8px;display:flex;gap:8px;margin-bottom:8px;width:100px}
.contact svg{width:8px;height:8px;flex:none}
.newsletter{left:485px;width:141px}
.newsletter p{margin-top:9px;font-size:6px;line-height:14px;padding-left:3px}
.newsletter .field{margin:5px 0 0 3px;width:138px;height:20px;border:1px solid #bbb;box-shadow:inset 0 1px 2px rgba(0,0,0,.12);font-size:6px;line-height:18px;padding-left:7px;color:#777}
.newsletter .btn{margin:11px 0 0 3px;width:49px;height:18px;line-height:18px}
.footer-rule{position:absolute;left:78px;top:148px;width:548px;height:1px;background:var(--line)}
.copyright{position:absolute;left:0;width:704px;top:160px;text-align:center;font-size:6px;color:var(--muted)}
</style>
</head>
<body>

<header class="site-header">
  <div class="brand"><span class="brand-mark"></span><span class="brand-name">Brightmoor Labs</span></div>
  <nav class="main-nav">
    <a href="#" class="active">Home</a><a href="#">About</a><a href="#">Service</a><a href="#">Blog</a><a href="#">Contact</a>
  </nav>
</header>

<section class="hero" role="img" aria-label="Close-up photo of a light grey keyboard key with a padlock symbol">
  <h1 class="hero-title">Vakwerk Leerlijnen<br>voor ontwikkelaars</h1>
  <div class="hero-dots"><span class="on"></span><span></span><span></span></div>
</section>

<section class="welcome">
  <h1>Welcome to Brightmoor Labs</h1>
  <p>Nemo enim ipsam voluptatem quia voluptas sit aspernatur aut odit aut fugit, sed quia consequuntur magni dolores eos qui ratione voluptatem sequi nesciunt. Neque porro quisquam est, qui dolorem ipsum quia dolor sit amet, consectetur, adipisci velit, sed quia non numquam eius modi tempora incidunt ut labore et dolore magnam aliquam quaerat voluptatem. Ut enim ad minima veniam, quis nostrum exercitationem ullam corporis suscipit laboriosam, nisi ut aliquid ex ea commodi consequatur</p>
  <a href="#" class="btn">Read More</a>
</section>

<section class="trainings">
  <div class="training-grid">
    <article class="training-card">
      <svg viewBox="0 0 32 28" fill="var(--navy)"><path d="M9 13V8a5 5 0 0 1 10 0h-3a2 2 0 0 0-4 0v5z"/><rect x="7" y="12" width="18" height="14" rx="2"/></svg>
      <h2>Trainning 1</h2>
      <p>Nemo enim ipsam voluptatem quia voluptas sit asper-natur aut odit aut fugit, sed quia consequuntur magni dolores eos qui rationeexercitationem</p>
      <a href="#" class="btn">More Info</a>
    </article>
    <article class="training-card">
      <svg viewBox="0 0 32 28" fill="none" stroke="var(--navy)" stroke-width="2"><path d="M16 2a7 7 0 0 0-4 12.7V19h8v-4.3A7 7 0 0 0 16 2z"/><path d="M13 22h6M14 25h4" /><path d="M15 7a3 3 0 0 1 3 2" stroke-width="1.2"/></svg>
      <h2>Trainning 2</h2>
      <p>Nemo enim ipsam voluptatem quia voluptas sit asper-natur aut odit aut fugit, sed quia consequuntur magni dolores eos qui rationeexercitationem</p>
      <a href="#" class="btn">More Info</a>
    </article>
    <article class="training-card">
      <svg viewBox="0 0 32 28" fill="var(--navy)"><circle cx="12" cy="15" r="7"/><circle cx="12" cy="15" r="2.5" fill="#fff"/><circle cx="24" cy="7" r="4.5"/><circle cx="24" cy="7" r="1.5" fill="#fff"/><circle cx="24" cy="22" r="4.5"/><circle cx="24" cy="22" r="1.5" fill="#fff"/></svg>
      <h2>Trainning 3</h2>
      <p>Nemo enim ipsam voluptatem quia voluptas sit asper-natur aut odit aut fugit, sed quia consequuntur magni dolores eos qui rationeexercitationem</p>
      <a href="#" class="btn">More Info</a>
    </article>
    <article class="training-card">
      <svg viewBox="0 0 32 28" fill="var(--navy)"><ellipse cx="16" cy="4" rx="12" ry="3.5"/><path d="M4 7q12 6 24 0v4q-12 6-24 0zM4 14q12 6 24 0v4q-12 6-24 0zM4 21q12 6 24 0v3q-12 6-24 0z"/></svg>
      <h2>Security</h2>
      <p>Nemo enim ipsam voluptatem quia voluptas sit asper-natur aut odit aut fugit, sed quia consequuntur magni dolores eos qui rationeexercitationem</p>
      <a href="#" class="btn">More Info</a>
    </article>
    <article class="training-card">
      <svg viewBox="0 0 32 28" fill="none" stroke="var(--navy)" stroke-width="2.4"><path d="M10 7l-7 7 7 7M22 7l7 7-7 7M19 4l-6 20"/></svg>
      <h2>Developer</h2>
      <p>Nemo enim ipsam voluptatem quia voluptas sit asper-natur aut odit aut fugit, sed quia consequuntur magni dolores eos qui rationeexercitationem</p>
      <a href="#" class="btn">More Info</a>
    </article>
    <article class="training-card">
      <svg viewBox="0 0 32 28" fill="var(--navy)"><path d="M6 1h14v6H6z"/><path d="M6 1h13v26H6z"/><path d="M13 9h10l5 5v14H13z" stroke="#fff" stroke-width="1.5"/></svg>
      <h2>Workshop</h2>
      <p>Nemo enim ipsam voluptatem quia voluptas sit asper-natur aut odit aut fugit, sed quia consequuntur magni dolores eos qui rationeexercitationem</p>
      <a href="#" class="btn">More Info</a>
    </article>
  </div>
</section>

<footer class="site-footer">
  <div class="brand"><span class="brand-mark"></span><span class="brand-name">Brightmoor Labs</span></div>
  <div class="social"><span></span><span></span><span></span><span></span><span></span></div>

  <div class="footer-col quick-links">
    <h3>Quick Links</h3>
    <ul><li>Home</li><li>About us</li><li>Services</li><li>Blog</li><li>Contact us</li></ul>
  </div>

  <div class="footer-col contact">
    <h3>Contact Us</h3>
    <ul>
      <li><svg viewBox="0 0 8 8" fill="#555"><path d="M0 2q4-3 8 0v1H6V2H2v1H0zM1 4h6v4H1z"/></svg>020-555-0141/</li>
      <li><svg viewBox="0 0 8 8" fill="#555"><path d="M2 0h4v2H2zM0 2h8v4H0zM2 5h4v3H2z"/></svg>020-555-0187</li>
      <li><svg viewBox="0 0 8 8" fill="#555"><path d="M0 1h8v6H0z"/><path d="M0 1l4 3 4-3" stroke="#fff" fill="none"/></svg><u>info@brightmoorlabs.nl</u></li>
      <li><svg viewBox="0 0 8 8" fill="#555"><path d="M4 0a3 3 0 0 1 3 3c0 2-3 5-3 5S1 5 1 3a3 3 0 0 1 3-3z"/><circle cx="4" cy="3" r="1" fill="#fff"/></svg>#2868 Lorem ipsum dolor sit amet, consectetur</li>
    </ul>
  </div>

  <div class="footer-col newsletter">
    <h3>Subscribe Newsletter</h3>
    <p>Enter your email address to receive the latest news our blog.</p>
    <div class="field">Email Id</div>
    <a href="#" class="btn">SUBSCRIBE</a>
  </div>

  <div class="footer-rule"></div>
  <p class="copyright">©2016 brightmoorlabs.nl. All Rights Reserved.</p>
</footer>

</body>
</html>
```